Corinne Bracket tutoring Advertising package - flyers, posters, business card and logo

I am looking for a flyer design for my tutoring business, it needs to explain what tutoring services I offer, how much I charge, why my services are worthwhile, it should include some photos of me and the tutoring centre,

It needs to include my phone number and my website. It should quote from some of the testimonials I have received from parents and children.

My website is www.corinnebracket-example.com My Facebook page can be found at https://www.facebook.com/corinnebrackettutoring These pages include a range of photos and quotes that you can use.

I am not sure about the colours and designs that I would like, that's why I'm using Sketchmarket!
I'm looking to appeal to parents inform them of my skills and experience.

I'm charging $45 for sessions of an hour and 15 minutes. 2 sessions per week will cost $80. I tutor Monday to Friday afternoons and evenings along with all day Saturdays. The assessment is free.

I tutor children from K-9 in English and Maths. I'm mainly aiming at parents whose children are struggling a little bit at school although I can help children who are doing well too.
I am highly skilled at helping children who can't read, I have a comprehensive program, the Pemberly program, that specifically teaches children the skills they need to read fluently and successfully.

Similarly I have had a lot of experience at helping children improve their Maths skills. I am well resourced with a wide range of hands on resources, paper resources and electronic resources.

Children will get better GRESTO results if I tutor them (GRESTO is the national series of tests in Australia).

I'm after a DL double sided flyer, and an A4 flyer. I'm also looking for two A2 posters and two A3 posters. Finally, I want a business card too. I don't have a logo for the business and I'd love to have one!

Target Market(s)

Parents of school aged children

Industry/Entity Type

Education

Colors

Designer to choose colors to be used in the design.

Requirements
Must have
• my name, my photo, length and cost of my sessions, email and phone contact details. Subjects and age ranges that I teach, times that I tutor. Website and/or Facebook page references. Quotes from Testimonials
Nice to have
• The A2 and A3 posters should complement each other.

```html
<!DOCTYPE html>
<html lang="en">
<head>
<meta charset="utf-8">
<title>Corinne Bracket Private Tutor – DL Flyer</title>
<link rel="stylesheet" href="https://fonts.googleapis.com/css2?family=Roboto:ital,wght@0,300;0,400;0,700;0,900;1,700;1,900&family=Kalam:wght@400;700&family=Libre+Baskerville:wght@700&display=swap">
<style>
  :root{
    --page:#e9e6e4;
    --label:#3a3a3a;
    --magenta:#e5197b;
    --teal:#1fa08c;
    --teal-bar:#1b8fb0;
    --green-dark:#0f6b3a;
    --yellow:#ffe500;
    --red:#d0202a;
    --grey:#8f8f8f;
    --grey-dark:#555;
    --blue:#1373b8;
    --violet:#3b3fa8;
    --bubble-green:#1b7a3a;
    --bubble-red:#8c1420;
    --bubble-orange:#f39a1e;
    --white:#fff;
  }
  *{box-sizing:border-box;margin:0;padding:0}
  html,body{width:1200px;height:2400px;overflow:hidden}
  body{background:var(--page);font-family:"Roboto",Arial,sans-serif;position:relative}

  .side-label{position:absolute;left:0;width:1200px;text-align:center;font-family:"Libre Baskerville",Georgia,serif;font-weight:700;font-size:34px;letter-spacing:6px;color:var(--label)}
  .side-label--front{top:60px}
  .side-label--back{top:2300px}

  .flyer{position:absolute;left:220px;width:760px;height:980px;background:var(--white);overflow:hidden;box-shadow:0 6px 24px rgba(0,0,0,.18)}
  .flyer--front{top:130px}
  .flyer--back{top:1260px}

  /* FRONT */
  .hero-photo{position:absolute;left:0;top:0;width:760px;height:430px;background:linear-gradient(120deg,#d9d5cc 0%,#c8bfae 35%,#8fbf5c 62%,#d6cfc2 100%)}
  .years-number{position:absolute;left:125px;top:322px;font-size:178px;font-weight:900;line-height:1;letter-spacing:-6px;background:linear-gradient(180deg,#fff 0%,#fff 58%,#6a6a6a 100%);-webkit-background-clip:text;background-clip:text;color:transparent}
  .years-caption{position:absolute;left:58px;top:462px;font-size:34px;font-weight:300;color:var(--grey)}
  .tutor-name{position:absolute;left:20px;top:496px;font-size:58px;font-weight:700;color:var(--magenta);letter-spacing:-1px}
  .tutor-role{position:absolute;left:300px;top:560px;font-size:30px;color:var(--grey-dark)}
  .questions{position:absolute;left:20px;top:612px;font-size:16.5px;font-weight:700;color:var(--grey-dark);line-height:1.4}
  .headline{position:absolute;left:20px;top:688px;font-size:54px;font-weight:900;font-style:italic;color:var(--teal)}
  .statements{position:absolute;left:20px;top:766px;font-size:17px;font-weight:700;color:var(--grey-dark);line-height:1.4}
  .motivation{position:absolute;left:62px;top:818px;font-family:"Kalam",cursive;font-size:21px;color:var(--red);line-height:1.05;text-align:center}

  .price-badge{position:absolute;left:455px;top:450px;width:300px;height:300px}
  .price-badge svg{position:absolute;left:0;top:0}
  .price-badge__text{position:absolute;left:0;top:40px;width:300px;text-align:center;line-height:1}
  .price-badge__amount{font-size:54px;font-weight:700;color:var(--yellow)}
  .price-badge__amount sup{font-size:30px;vertical-align:top}
  .price-badge__for{font-size:18px;color:var(--white)}
  .price-badge__minutes{font-size:54px;font-weight:900;color:var(--white)}
  .price-badge__unit{font-size:20px;color:var(--white)}
  .price-badge__note{font-size:20px;color:var(--yellow);font-weight:700}

  .assessment-tag{position:absolute;left:440px;top:728px;width:140px;height:80px;border-radius:50%;background:var(--yellow);display:flex;flex-direction:column;align-items:center;justify-content:center;transform:rotate(-6deg);z-index:2;line-height:1}
  .assessment-tag span{font-size:15px;font-weight:700;color:var(--red)}
  .assessment-tag strong{font-size:28px;font-weight:900;color:var(--red)}

  .hours-bar{position:absolute;left:490px;top:768px;width:270px;height:106px;background:var(--teal-bar);border-top-left-radius:40px;color:var(--white);font-size:17px;line-height:1.22;text-align:right;padding:12px 14px 0 14px;white-space:nowrap}

  .results-line{position:absolute;left:0;top:884px;width:760px;text-align:center;font-size:28px;color:var(--violet)}
  .results-line strong{color:var(--magenta);font-weight:900}

  .contact-bar{position:absolute;left:0;bottom:0;width:760px;height:58px;background:var(--blue);display:flex;align-items:center;justify-content:center;gap:10px;font-size:30px;color:var(--yellow)}
  .contact-bar__web{font-weight:700}

  /* BACK */
  .shelf-photo{position:absolute;left:0;top:0;width:272px;height:980px;background:linear-gradient(180deg,#6b3e22 0%,#c9b49a 18%,#7aa0c4 40%,#a85b36 60%,#c23c8e 78%,#3b6fbf 88%,#2c1c12 100%)}
  .bubble{position:absolute;border-radius:50%;color:var(--white);text-align:center;display:flex;align-items:center;justify-content:center;font-size:10.5px;line-height:1.25;font-weight:700}
  .bubble i{position:absolute;border-radius:50%}
  .bubble--green{left:285px;top:30px;width:210px;height:140px;background:var(--bubble-green);padding:16px 28px}
  .bubble--green i{background:var(--bubble-green)}
  .bubble--red{left:520px;top:70px;width:235px;height:215px;background:var(--bubble-red);padding:28px 32px;font-size:10px}
  .bubble--red i{background:var(--bubble-red)}
  .bubble--orange{left:400px;top:280px;width:150px;height:95px;background:var(--bubble-orange);color:var(--bubble-red);font-size:13px;padding:10px 18px}
  .bubble--orange i{background:var(--bubble-orange)}
  .attribution{position:absolute;font-size:13px;color:var(--grey-dark);line-height:1.2}
  .attribution b{display:block;color:#333}

  .services{position:absolute;left:290px;top:455px;width:455px;list-style:none}
  .services li{position:relative;padding-left:28px;margin-bottom:22px;font-size:14.5px;font-weight:700;color:var(--grey-dark);line-height:1.3;text-align:justify}
  .services li::before{content:"";position:absolute;left:0;top:4px;width:14px;height:14px;border-radius:50%;background:var(--teal)}
  .services li:last-child{width:250px;text-align:left}
  .desk-photo{position:absolute;left:560px;top:820px;width:200px;height:160px;background:linear-gradient(160deg,#f4f4f4 0%,#9fc0dc 45%,#c9874e 100%)}
</style>
</head>
<body>

<div class="side-label side-label--front">FRONT</div>

<section class="flyer flyer--front">
  <div class="hero-photo" role="img" aria-label="Photo of the tutor smiling in the tutoring room with bookshelves and a poster"></div>
  <div class="years-number">25</div>
  <div class="years-caption">years experienced</div>
  <h1 class="tutor-name">Corinne Bracket</h1>
  <div class="tutor-role">Private Tutor</div>

  <p class="questions">Is your child struggling at school?<br>Would you like to see your child succeed at school?<br>Do you want them to enjoy learning?</p>
  <h2 class="headline">It can happen!</h2>
  <p class="statements">I am a teacher, I am a father,<br>I am a lifelong learner and I can help your child grow.</p>
  <p class="motivation">Your child will experience success<br>and that is strongly motivating.</p>

  <div class="price-badge">
    <svg width="300" height="300" viewBox="0 0 300 300">
      <defs>
        <path id="badge-arc" d="M 32 150 A 118 118 0 0 0 268 150"/>
      </defs>
      <polygon fill="#0f6b3a" points="150,2 164,24 185,7 193,32 218,21 220,47 246,43 242,69 268,73 256,96 281,109 263,127 286,150 263,173 281,191 256,204 268,227 242,231 246,257 220,253 218,279 193,268 185,293 164,276 150,298 136,276 115,293 107,268 82,279 80,253 54,257 58,231 32,227 44,204 19,191 37,173 14,150 37,127 19,109 44,96 32,73 58,69 54,43 80,47 82,21 107,32 115,7 136,24"/>
      <text font-family="Roboto, sans-serif" font-weight="700" font-size="19" fill="#fff" dy="-2"><textPath href="#badge-arc" startOffset="50%" text-anchor="middle">first session will no longer be free</textPath></text>
    </svg>
    <div class="price-badge__text">
      <div class="price-badge__amount"><sup>$</sup>45</div>
      <div class="price-badge__for">for</div>
      <div class="price-badge__minutes">75</div>
      <div class="price-badge__unit">minutes</div>
      <div class="price-badge__note">this year</div>
    </div>
  </div>

  <div class="assessment-tag"><span>The assessment</span><span>is <strong>free</strong></span></div>
  <div class="hours-bar">Monday, Wednesday,<br>Thursday and Friday<br>afternoons and evenings<br>along with all day Saturdays</div>

  <p class="results-line">Children will get better <strong>GRESTO</strong> results if I tutor them</p>
  <div class="contact-bar"><span class="contact-bar__web">www.corinnebracket-example.com</span><span>|</span><span>0400 555 019</span></div>
</section>

<section class="flyer flyer--back">
  <div class="shelf-photo" role="img" aria-label="Photo of bookshelves filled with children's books and reading series"></div>

  <div class="bubble bubble--green">"Corinne is a teacher who understands how children think, who tailors her teaching to the child's individual learning style and a teacher who shares her passion for learning with her students. My son loved his lessons."
    <i style="width:16px;height:16px;left:120px;top:142px"></i><i style="width:10px;height:10px;left:108px;top:160px"></i><i style="width:6px;height:6px;left:100px;top:172px"></i>
  </div>
  <div class="attribution" style="left:300px;top:200px"><b>Mara Ellison,</b>celebrant and parent</div>

  <div class="bubble bubble--red">Corinne is a wonderful teacher. She is caring, patient and is able to explain things in a way that is easy for a child to understand. Furthermore she is encouraging, supportive and gives a child the space to learn in their own style and pace. I would highly recommend her for any child who needs a little bit of extra help or for those who want to progress ahead.
    <i style="width:16px;height:16px;left:80px;top:216px"></i><i style="width:10px;height:10px;left:70px;top:236px"></i><i style="width:6px;height:6px;left:64px;top:250px"></i>
  </div>
  <div class="attribution" style="left:620px;top:320px"><b>Priya Dane,</b>mother and accountant</div>

  <div class="bubble bubble--orange">"She is smart and cool and the best teacher in the world!"
    <i style="width:12px;height:12px;left:50px;top:98px"></i><i style="width:7px;height:7px;left:44px;top:112px"></i>
  </div>
  <div class="attribution" style="left:460px;top:400px"><b>Tessa Moore,</b>student</div>

  <ul class="services">
    <li>I use the Pemberly Method for reading. It works because it is clear, logical and ensures that young readers experience success. It is based upon the fact that English is an alphabetic language and has been developed by working with children!</li>
    <li>I help children learn Maths in a clear, logical manner. I help them learn simple, effective techniques that will develop their speed and accuracy in Maths. I use technology and hands on resources to develop their understanding of concepts.</li>
    <li>I know how to use technology with your children. I use professional, quality programs that are engaging and useful. I provide fast computers and wireless Internet when to support your child's learning.</li>
    <li>I am a skilled and experienced teacher. I enjoy working with children and they respond well to me. I love learning and it's natural for me to share that love with children.</li>
    <li>I offer a practical Science course that engages children and develops their understanding and knowledge of Science through conducting and analysing experiments.</li>
  </ul>

  <div class="desk-photo" role="img" aria-label="Photo of the tutor seated at a desk with a computer"></div>
</section>

<div class="side-label side-label--back">BACK</div>

</body>
</html>
```